LA Billboard Project for Brisk Lending

We are running three different billboards around LA, and we need someone to take the mock-ups I've created and bring this campaign to life. Whatever wording is on the mock-ups should stay the same in the ads you create, but feel free to get creative with layout and style. I've attached our mock-ups, our style guide, our logo, and the necessary specs for the billboards. If you have any questions, feel free to reach out!

```html
<!DOCTYPE html>
<html lang="en">
<head>
<meta charset="utf-8">
<title>Brisk Lending Billboard – Mortgage Strategy</title>
<link href="https://fonts.googleapis.com/css2?family=Bebas+Neue&display=swap" rel="stylesheet">
<style>
  :root {
    --brand-blue: #2a3fa8;
    --headline-white: #ffffff;
    --url-yellow: #f7dc0a;
    --accent-cyan: #3fc6d6;
    --sky-top: #8e8cc8;
    --sky-mid: #7472b4;
    --city-low: #4b4d8e;
    --ground: #6b6ca2;
    --beam: rgba(128, 224, 238, 0.62);
  }
  * { margin: 0; padding: 0; box-sizing: border-box; }
  html, body {
    width: 1200px;
    height: 674px;
    overflow: hidden;
    background: #ffffff;
  }
  .billboard {
    position: relative;
    width: 1200px;
    height: 674px;
    background: var(--brand-blue);
    font-family: "Bebas Neue", "Oswald", sans-serif;
    overflow: hidden;
  }
  .city-photo {
    position: absolute;
    left: 395px;
    top: 21px;
    width: 791px;
    height: 630px;
    background: linear-gradient(180deg,
      var(--sky-top) 0%,
      var(--sky-mid) 30%,
      var(--city-low) 55%,
      var(--ground) 100%);
  }
  .light-beam {
    position: absolute;
    left: 0;
    top: 0;
    width: 1200px;
    height: 674px;
    pointer-events: none;
  }
  .headline {
    position: absolute;
    left: 33px;
    top: 22px;
    color: var(--headline-white);
    font-size: 80px;
    line-height: 100px;
    letter-spacing: 4px;
    font-weight: 400;
  }
  .website {
    position: absolute;
    left: 33px;
    top: 388px;
    color: var(--url-yellow);
    font-size: 60px;
    line-height: 60px;
    letter-spacing: 3px;
  }
  .brand-name {
    position: absolute;
    left: 33px;
    top: 560px;
    display: flex;
    align-items: center;
    gap: 14px;
    color: var(--headline-white);
    font-size: 54px;
    line-height: 54px;
    letter-spacing: 2px;
  }
  .brand-mark {
    width: 26px;
    height: 26px;
    background: var(--accent-cyan);
  }
</style>
</head>
<body>
  <main class="billboard">
    <div class="city-photo" role="img" aria-label="Aerial view of a downtown city skyline with snow-capped mountains behind, tinted in blue-violet"></div>

    <svg class="light-beam" viewBox="0 0 1200 674" aria-hidden="true">
      <polygon points="422,651 1186,386 1186,651" fill="var(--beam)"/>
    </svg>

    <h1 class="headline">What’s your<br>mortgage<br>strategy?</h1>
    <p class="website">BRISKREFI.COM</p>

    <div class="brand-name">
      <span class="brand-mark"></span>
      <span>Brisk Lending</span>
    </div>
  </main>
</body>
</html>
```